Licensed School Psychologist Business Card Design (may be single or double sided)

In an empathetic and nurturing environment, I conduct comprehensive psycho-educational evaluations for children and adolescents who may be experiencing academic, social/emotional challenges, and stressors in their lives. Given the collection of data and information, recommendations, supports, and strategies are created and tailored to the strengths and weaknesses of the children/adolescents as well as their families.

Industry/Entity Type

Business

Contact Information for Business Card

Bright-Path Learning Assessments
Helen Marchetti, MEd; MA
Licensed School Psychologist
482 Tolliver Lane, Suite #3
Williamsburg, VA 23185
P: 757 612-3094 F: 757 612-3157

```html
<!DOCTYPE html>
<html lang="en">
<head>
<meta charset="utf-8">
<title>Bright-Path Learning Assessments — Business Card</title>
<link rel="stylesheet" href="https://fonts.googleapis.com/css2?family=Oswald:wght@400;500;600;700&display=swap">
<style>
  :root {
    --stage: #e9e6e2;
    --card-white: #ffffff;
    --card-black: #1b1c1e;
    --card-black-deep: #0e0f10;
    --ink-dark: #3a3a3c;
    --accent-orange: #e07a3a;
    --accent-copper: #d98a4a;
    --mark-grey: #55575a;
  }
  * { box-sizing: border-box; margin: 0; padding: 0; }
  html, body { width: 1200px; height: 871px; overflow: hidden; }
  body {
    background: var(--stage);
    font-family: "Oswald", "Arial Narrow", sans-serif;
    display: flex;
    align-items: center;
    justify-content: center;
  }
  .card-set {
    display: flex;
    gap: 40px;
  }
  .card {
    width: 560px;
    height: 320px;
    border-radius: 4px;
    box-shadow: 0 6px 18px rgba(0,0,0,0.18);
    position: relative;
    overflow: hidden;
  }

  /* Front side */
  .card--front {
    background: var(--card-white);
    display: flex;
    align-items: center;
    padding: 0 34px;
  }
  .brand {
    width: 215px;
    display: flex;
    align-items: center;
    gap: 10px;
  }
  .brand__dot {
    flex: 0 0 18px;
    height: 18px;
    border-radius: 50%;
    background: var(--accent-copper);
  }
  .brand__name {
    color: var(--accent-copper);
    font-weight: 500;
    font-size: 19px;
    line-height: 1.15;
    text-transform: uppercase;
    letter-spacing: 0.04em;
  }
  .divider {
    width: 2px;
    height: 170px;
    background: var(--accent-orange);
    margin: 0 22px 0 14px;
  }
  .contact { color: var(--ink-dark); }
  .contact__name {
    font-weight: 700;
    font-size: 24px;
    letter-spacing: 0.02em;
    line-height: 1.1;
  }
  .contact__title {
    color: var(--accent-orange);
    font-weight: 500;
    font-size: 13.5px;
    margin-bottom: 10px;
  }
  .contact__row {
    display: flex;
    align-items: flex-start;
    gap: 9px;
    font-weight: 500;
    font-size: 14px;
    line-height: 1.4;
    margin-bottom: 4px;
  }
  .contact__icon {
    flex: 0 0 14px;
    width: 14px;
    height: 14px;
    margin-top: 3px;
    fill: var(--accent-orange);
  }

  /* Back side */
  .card--back {
    background: radial-gradient(ellipse at 45% 40%, var(--card-black) 0%, var(--card-black-deep) 100%);
    display: flex;
    align-items: center;
    justify-content: center;
  }
  .back-brand {
    display: flex;
    align-items: center;
    gap: 14px;
  }
  .back-brand__square {
    width: 22px;
    height: 22px;
    background: var(--mark-grey);
  }
  .back-brand__name {
    color: var(--mark-grey);
    font-weight: 500;
    font-size: 26px;
    line-height: 1.15;
    text-transform: uppercase;
    letter-spacing: 0.08em;
  }
</style>
</head>
<body>
  <main class="card-set">
    <section class="card card--front" aria-label="Card front">
      <div class="brand">
        <span class="brand__dot"></span>
        <span class="brand__name">Bright-Path Learning Assessments</span>
      </div>
      <div class="divider"></div>
      <div class="contact">
        <p class="contact__name">Helen Marchetti</p>
        <p class="contact__title">MEd; MA Licensed School Psychologist</p>
        <p class="contact__row">
          <svg class="contact__icon" viewBox="0 0 14 14" aria-hidden="true"><path d="M7 0a5 5 0 0 0-5 5c0 3.6 5 9 5 9s5-5.4 5-9a5 5 0 0 0-5-5zm0 7a2 2 0 1 1 0-4 2 2 0 0 1 0 4z"/></svg>
          <span>482 Tolliver Lane,<br>Suite #3 Williamsburg, VA 23185</span>
        </p>
        <p class="contact__row">
          <svg class="contact__icon" viewBox="0 0 14 14" aria-hidden="true"><path d="M1 4c0-1.5 2.5-2.5 6-2.5S13 2.5 13 4v1.2h-3V3.8H4v1.4H1z"/><path d="M2.5 6.5h9l1 6h-11z"/></svg>
          <span>757 612-3094</span>
        </p>
        <p class="contact__row">
          <svg class="contact__icon" viewBox="0 0 14 14" aria-hidden="true"><rect x="3.5" y="1" width="7" height="4"/><rect x="1" y="5.5" width="12" height="6" rx="1"/><rect x="3.5" y="10" width="7" height="3"/></svg>
          <span>757 612-3157</span>
        </p>
      </div>
    </section>

    <section class="card card--back" aria-label="Card back">
      <div class="back-brand">
        <span class="back-brand__square"></span>
        <span class="back-brand__name">Bright-Path<br>Learning Assessments</span>
      </div>
    </section>
  </main>
</body>
</html>
```